Web Design Project - Lunorexa

I want to take the existing logo, add a strapline to it and update the logo files. I then need to design powerpoint template and MS Word template for our collateral as well as 9cm x 5cm business card design for 5 people. I then want to design the website look and feel, and get whatever advice I can on coding it and next steps. Consistent message, innovation and technical ability are what I'm pushing. We are supplying Water Companies, Oil and Gas and Contractors with machinery and products to repair pipelines without digging up the ground, otherwise known as trenchless rehabilitation. I will need some help on content as well. one of our partners is www.kvolbramet.example we need to include their products and can use their content. I will need the ability to add to the site , I think it is called CMS.
Updates

Thanks for your input so far, the strap line is Renewable Infrastructure Solutions. I want to work it into the logo to make it seem part of it as opposed to just added text.

I have uploaded the existing business card design, I like this so, I want to add to this design rather than change it, it needs to be 9cm x 5.5cm. I would like to see some vertical designs as well as horizontal.

apologies I have been away, I will provide feedback ASAP

Target Market(s)

contractors, government, engineers, urban planners, environmentalists, degree level

Industry/Entity Type

Business

Requirements
Must have
• It must be compliant with all ios devices and fully windows and mac compatible.
No flash
Nice to have
• some sort of dynamic content

```html
<!DOCTYPE html>
<html lang="en">
<head>
<meta charset="utf-8">
<title>Lunorexa — Home</title>
<link href="https://fonts.googleapis.com/css2?family=Roboto+Condensed:wght@400;500&family=PT+Sans:wght@400;700&display=swap" rel="stylesheet">
<style>
:root{
  --red:#d9412b;
  --bar-top:#6a6b70;
  --bar-bottom:#4e4f54;
  --text:#4a4a4a;
  --muted:#777;
  --footer:#e4e4e4;
  --white:#fff;
}
*{margin:0;padding:0;box-sizing:border-box}
html,body{width:1200px;height:919px;overflow:hidden;background:var(--white)}
.stage{position:relative;width:1400px;height:1072px;transform:scale(.857143);transform-origin:0 0;font-family:"PT Sans",sans-serif;color:var(--text)}
.abs{position:absolute}
.cond{font-family:"Roboto Condensed",sans-serif}

.brand{left:212px;top:28px;display:flex;align-items:center;gap:14px}
.brand-name{font-family:"PT Sans",sans-serif;font-weight:700;font-size:27px;letter-spacing:1.5px;color:#8a8a8e}
.brand-mark{width:42px;height:42px;background:var(--red)}
.call{right:210px;top:60px;font-size:18px;color:#888}
.call b{color:var(--red);font-weight:400}

.nav{left:211px;top:106px;width:980px;height:37px;background:linear-gradient(var(--bar-top),var(--bar-bottom));display:flex}
.nav a{color:var(--white);text-decoration:none;font-size:13px;line-height:37px;text-align:center;font-family:"Roboto Condensed",sans-serif}
.nav a.active{background:var(--red)}

.slider{left:211px;top:150px;width:980px;height:363px;background:linear-gradient(160deg,#8a7570,#5e4a47 45%,#3d302e 80%,#6a5855)}
.slider-arrow{position:absolute;top:165px;width:29px;height:29px;border-radius:50%;background:rgba(40,40,40,.75);display:flex;align-items:center;justify-content:center}
.slide-caption{position:absolute;left:0;bottom:0;width:100%;height:77px;background:rgba(40,36,36,.7);color:var(--white);padding:16px 17px}
.slide-caption h1{font-family:"Roboto Condensed",sans-serif;font-weight:400;font-size:21px;letter-spacing:.2px}
.slide-caption p{font-size:10.5px;margin-top:8px;letter-spacing:-.2px}

.section-head{height:31px;background:linear-gradient(var(--bar-top),var(--bar-bottom));border-left:5px solid var(--red);position:relative}
.section-head::before{content:"";position:absolute;left:0;top:0;width:2px;height:100%;background:var(--white)}
.section-head h2{font-family:"Roboto Condensed",sans-serif;font-weight:400;font-size:14px;color:var(--white);line-height:31px;padding-left:14px}

.card{top:533px;width:228px}
.card-photo{margin-top:9px;width:226px;height:106px;border:3px solid #e6e6e6}
.card p{font-size:10.5px;line-height:18px;padding:8px 4px 0 5px}
.btn{display:inline-block;width:75px;height:23px;border-radius:3px;background:linear-gradient(#6d6e72,#505155);color:#ddd;font-size:10.5px;line-height:23px;text-align:center}
.card .btn{margin:9px 0 0 153px}

.about-head{left:211px;top:823px;width:980px}
.about-text{left:211px;top:873px;width:730px;font-size:10.5px;line-height:18px;text-align:justify}
.about-btn{left:212px;top:958px}
.about-photo{left:959px;top:876px;width:232px;height:102px;border:3px solid #e6e6e6;background:linear-gradient(120deg,#3b4a7a,#7d8db0 40%,#2c3660 70%,#8a7a60)}

.footer{left:211px;top:1005px;width:980px;height:67px;background:var(--footer)}
.footer-links{position:absolute;left:25px;top:19px;font-size:9.5px;color:#555;display:flex;font-family:"Roboto Condensed",sans-serif}
.footer-links span.sep{margin:0 20px}
.copyright{position:absolute;left:25px;top:39px;font-size:9px;color:#555}
.follow{position:absolute;left:804px;top:29px;font-size:10px;color:#555}
.social{position:absolute;top:20px;width:27px;height:27px;border-radius:4px}
</style>
</head>
<body>
<div class="stage">
  <header>
    <div class="abs brand"><span class="brand-name">LUNOREXA</span><span class="brand-mark"></span></div>
    <div class="abs call cond">CALL US : <b>( 2222 ) 222 222</b></div>
  </header>

  <nav class="abs nav">
    <a class="active" style="width:86px">HOME</a>
    <a style="width:146px">ABOUT US</a>
    <a style="width:102px">SERVICES</a>
    <a style="width:148px">PRODUCTS</a>
    <a style="width:108px">TRAININGS</a>
    <a style="width:154px">STANDERDS</a>
    <a style="width:86px">NEWS</a>
    <a style="width:150px">CONTACT US</a>
  </nav>

  <section class="abs slider" role="img" aria-label="Stacked steel pipes in a storage yard">
    <span class="slider-arrow" style="left:8px"><svg width="10" height="12" viewBox="0 0 10 12"><path d="M7 1 2 6l5 5" fill="none" stroke="#bbb" stroke-width="1.5"/></svg></span>
    <span class="slider-arrow" style="right:6px"><svg width="10" height="12" viewBox="0 0 10 12"><path d="M3 1l5 5-5 5" fill="none" stroke="#bbb" stroke-width="1.5"/></svg></span>
    <div class="slide-caption">
      <h1>YOU DON'T NEED A SHOVEL TO START AN UNDERGROUND REVOLUTION</h1>
      <p>FOR MOST, THERE IS AN “OUT OF SIGHT, OUT OF MIND” MENTALITY REGARDING THE NEGATIVE IMPACTS OF DETERIORATING WASTEWATER PIPES. UNLESS THEY ARE CONFRONTED WITH TOTAL FAILURE,</p>
    </div>
  </section>

  <article class="abs card" style="left:211px">
    <div class="section-head"><h2>WATER COMPANIES</h2></div>
    <div class="card-photo" role="img" aria-label="Silver water pipework against a blue sky" style="background:linear-gradient(90deg,#3a4a70,#c9ced6 35%,#6d7888 60%,#d8dde4 80%,#2d4d9a)"></div>
    <p>For most, there is an “out of sight, out of mind” mentality regarding the negative impacts of deteriorating wastewater pipes. Unless they are confronted with total failure,</p>
    <span class="btn">Read More</span>
  </article>
  <article class="abs card" style="left:463px">
    <div class="section-head"><h2>OIL AND GAS</h2></div>
    <div class="card-photo" role="img" aria-label="Pale blue gas storage tanks" style="background:linear-gradient(120deg,#a9cfe8,#6fa8d4 50%,#d6ebf6 75%,#4e8fc4)"></div>
    <p>For most, there is an “out of sight, out of mind” mentality regarding the negative impacts of deteriorating wastewater pipes. Unless they are confronted with total failure,</p>
    <span class="btn">Read More</span>
  </article>
  <article class="abs card" style="left:714px">
    <div class="section-head"><h2>CONTRACTORS WITH MACHINERY</h2></div>
    <div class="card-photo" role="img" aria-label="Rows of steel pipe ends" style="background:linear-gradient(160deg,#5a3a3c,#b9a7a8 40%,#3a2426 70%,#8a7273)"></div>
    <p>For most, there is an “out of sight, out of mind” mentality regarding the negative impacts of deteriorating wastewater pipes. Unless they are confronted with total failure,</p>
    <span class="btn">Read More</span>
  </article>
  <article class="abs card" style="left:965px">
    <div class="section-head"><h2>REPAIR PIPELINES</h2></div>
    <div class="card-photo" role="img" aria-label="Welder repairing a pipeline" style="background:linear-gradient(130deg,#1e2f70,#4a63b8 45%,#c4d4f2 60%,#2a3d86)"></div>
    <p>For most, there is an “out of sight, out of mind” mentality regarding the negative impacts of deteriorating wastewater pipes. Unless they are confronted with total failure,</p>
    <span class="btn">Read More</span>
  </article>

  <section>
    <div class="abs about-head section-head"><h2>ABOUT LUNOREXA</h2></div>
    <p class="abs about-text">One of the most important areas for significant global impact lies beneath us. The aging and decaying infrastructure of water and wastewater pipelines around the world presents major challenges and abundant opportunities for positive change. We are driven to deliver the best practices to the protection of human health and the environment. Kvolbramet, a market leader in the development and delivery of high performing, cost-effective wastewater and potable water rehabilitation systems renowned for their environmental compatibility and dedication to quality, one-source solutions.</p>
    <span class="abs btn about-btn">Read More</span>
    <div class="abs about-photo" role="img" aria-label="Two engineers in hard hats at an industrial plant"></div>
  </section>

  <footer class="abs footer">
    <div class="footer-links">
      <span>HOME</span><span class="sep">|</span><span>ABOUT US</span><span class="sep">|</span><span>SERVICES</span><span class="sep">|</span><span>PRODUCTS</span><span class="sep">|</span><span>TRAININGS</span><span class="sep">|</span><span>STANDERDS</span><span class="sep">|</span><span>NEWS</span><span class="sep">|</span><span>CONTACT US</span>
    </div>
    <div class="copyright">COPYRIGHT © 2013 LUNOREXA ALL RIGHTS RESERVED.</div>
    <div class="follow">FOLLOW US :</div>
    <span class="social" style="left:872px;background:#4a6fb0"></span>
    <span class="social" style="left:904px;background:#45a8d8"></span>
    <span class="social" style="left:936px;background:#3d7ab8"></span>
  </footer>
</div>
</body>
</html>
```